Quiet Harbor Hours Podcast Artwork

I need a cover for my podcast Quiet Harbor Hours that is clean, modern, and minimalist, but not too feminine

Target Market(s)

People struggling with fertility particularly women who are between the ages of 35-45 though there is a small set of listeners who are men

Requirements
Must have
• Embryo in the Zero
Should not have
• No script text

```html
<!DOCTYPE html>
<html lang="en">
<head>
<meta charset="utf-8">
<title>Quiet Harbor Hours Podcast Cover</title>
<link rel="stylesheet" href="https://fonts.googleapis.com/css2?family=Anton&family=Montserrat:wght@400&display=swap">
<style>
  :root {
    --paper: #ffffff;
    --plum-top: #56455a;
    --plum-bottom: #28222b;
    --cream: #f7e3da;
    --sage: #9dab8a;
    --skin: #f08a74;
    --dress: #f6b3ad;
    --hair: #06032f;
  }
  html, body {
    margin: 0;
    padding: 0;
    width: 1200px;
    height: 1200px;
    overflow: hidden;
    background: var(--paper);
  }
  .cover {
    position: relative;
    width: 1200px;
    height: 1200px;
    background: var(--paper);
    overflow: hidden;
  }
  .cover__panel {
    position: absolute;
    left: 39px;
    top: 38px;
    width: 1122px;
    height: 1124px;
    background: linear-gradient(180deg, var(--plum-top) 0%, var(--plum-bottom) 100%);
  }
  .cover__figure {
    position: absolute;
    left: 0;
    top: 100px;
    width: 460px;
    height: 1100px;
    border-radius: 200px 230px 0 0;
    background: linear-gradient(180deg, var(--hair) 0%, var(--hair) 28%, var(--skin) 45%, var(--dress) 100%);
  }
  .cover__title {
    position: absolute;
    left: 490px;
    top: 154px;
    width: 625px;
    height: 577px;
    margin: 0;
    display: flex;
    flex-direction: column;
    justify-content: center;
    align-items: center;
    gap: 44px;
    font-family: "Anton", "Oswald", sans-serif;
    font-weight: 400;
    color: var(--cream);
    text-transform: uppercase;
  }
  .cover__title-line {
    display: block;
    line-height: 1;
  }
  .cover__title-line--quiet { font-size: 228px; letter-spacing: 4px; }
  .cover__title-line--harbor { font-size: 186px; letter-spacing: 2px; }
  .cover__subtitle {
    position: absolute;
    left: 490px;
    top: 752px;
    width: 620px;
    margin: 0;
    text-align: center;
    font-family: "Anton", "Oswald", sans-serif;
    font-size: 166px;
    line-height: 1;
    color: var(--sage);
    letter-spacing: 40px;
    text-indent: 40px;
    text-transform: uppercase;
  }
  .cover__rule {
    position: absolute;
    left: 490px;
    top: 941px;
    width: 620px;
    height: 1px;
    background: var(--cream);
    opacity: 0.7;
  }
  .cover__label {
    position: absolute;
    left: 709px;
    top: 972px;
    width: 420px;
    margin: 0;
    text-align: right;
    font-family: "Montserrat", sans-serif;
    font-size: 56px;
    line-height: 1;
    letter-spacing: 19px;
    color: var(--cream);
  }
</style>
</head>
<body>
  <div class="cover">
    <div class="cover__panel"></div>
    <div class="cover__figure" role="img" aria-label="Illustration of an expectant woman in a pink patterned dress looking down and cradling her belly, with a sleeping baby shown inside"></div>
    <h1 class="cover__title">
      <span class="cover__title-line cover__title-line--quiet">Quiet</span>
      <span class="cover__title-line cover__title-line--harbor">Harbor</span>
    </h1>
    <p class="cover__subtitle">Hours</p>
    <div class="cover__rule"></div>
    <p class="cover__label">PODCAST</p>
  </div>
</body>
</html>
```